Pagina Lartécnica

The Lartécnica is a company dealing with leasing and selling real estate. The current site can be accessed at www.lartecnica-exemplo.com.br. We intend to redesign the look of the site and for that we would like to redesign the home page and the page with information and pictures of the property. The homepage should maintain the characteristics of the current common design simple, short and straightforward. The page with the data of the properties should be accessed with two changes page as it is currently running. The search from the map by region and should be maintained.
The page containing the information of the property will provide a total of 15 small pictures that when clicked will appear in larger size. The colors to be used should be orange, blue, black and white. The map can be maintained in the current colors.
Updates

Project Deadline Extended
Reason: Payment guarante!!

Payment guaranteed. Deadline for submission of designs April 27.

Industry/Entity Type

Real Estate

Requirements
Must have
• Search by map regions and search box
address
keep colors from the current page
phones
clean look
Nice to have
• clean look
Should not have
• We like the current page. We just want to make it compatible with modern and new design trends and monitors.

```html
<!DOCTYPE html>
<html lang="pt-BR">
<head>
<meta charset="utf-8">
<title>Lartécnica – Imóveis</title>
<link rel="stylesheet" href="https://fonts.googleapis.com/css2?family=Open+Sans:wght@400;600;700&display=swap">
<style>
:root{
  --orange:#f7870f;
  --orange-dark:#e57605;
  --navy:#2e4a72;
  --navy-dark:#223a5e;
  --title-blue:#2b4a78;
  --map-light:#a9c1de;
  --map-dark:#2f4a72;
  --page-bg:#eef0f2;
  --text:#222;
  --footer-text:#a9bcd6;
  --alert-bg:#f3dcdc;
  --alert-red:#b30f0f;
  --white:#fff;
}
*{box-sizing:border-box;margin:0;padding:0}
html,body{width:1200px;height:835px;overflow:hidden}
body{position:relative;font-family:"Open Sans",Arial,sans-serif;color:var(--text);background:var(--page-bg)}
.abs{position:absolute}
.backdrop{left:0;top:0;width:1200px;height:640px;background:linear-gradient(90deg,#f3f4f4,#e9ecef 60%,#e3e8ee)}
.sidebar{left:140px;top:0;width:238px;height:562px;background:var(--orange)}
.sidebar-shadow{left:135px;top:566px;width:250px;height:18px;border-radius:50%;background:radial-gradient(ellipse at center,rgba(0,0,0,.28),rgba(0,0,0,0) 70%)}
.brand{left:131px;top:29px;width:257px;height:88px;background:var(--white);box-shadow:0 3px 6px rgba(0,0,0,.25);display:flex;align-items:center;justify-content:center;gap:10px}
.brand-mark{width:14px;height:14px;background:var(--orange)}
.brand-name{font-weight:700;font-size:26px;color:var(--title-blue)}
.main-menu{left:158px;top:173px;list-style:none}
.main-menu li{height:28px;line-height:20px;color:var(--white);font-size:14px;font-weight:600;text-shadow:0 1px 1px rgba(0,0,0,.3);padding-left:16px;position:relative}
.main-menu li::before{content:"";position:absolute;left:0;top:7px;border-left:5px solid #fff;border-top:3px solid transparent;border-bottom:3px solid transparent}
.sidebar-rule{left:140px;top:457px;width:238px;height:2px;background:rgba(255,255,255,.35);border-bottom:1px solid rgba(0,0,0,.08)}
.phone-icon{left:160px;top:496px}
.phones{left:211px;top:496px;color:var(--white);font-weight:700;font-size:17px;line-height:22px;text-shadow:0 1px 1px rgba(0,0,0,.3)}
.account-links{left:986px;top:7px;font-size:11px;color:#333}
.search-panel{left:397px;top:29px;width:665px;height:88px;background:rgba(255,255,255,.85)}
.section-title{font-size:13px;font-weight:600;color:var(--title-blue)}
.select-box{left:425px;top:67px;width:184px;height:26px;border:1px solid #ccc;border-radius:3px;background:#fff;font-size:12px;color:#999;padding:4px 9px}
.select-box::after{content:"";position:absolute;right:10px;top:10px;border-top:5px solid #555;border-left:4px solid transparent;border-right:4px solid transparent}
.check{width:15px;height:15px;border:1px solid #ccc;border-radius:3px;background:#fff}
.check.on{background:#3c9ae0;box-shadow:inset 0 0 0 2px #fff;border-color:#aaa}
.check-label{font-size:13px;color:#333}
.search-btn{left:904px;top:64px;width:104px;height:31px;border-radius:4px;background:linear-gradient(#ffb13a,var(--orange-dark));color:#fff;font-weight:700;font-size:15px;display:flex;align-items:center;justify-content:center;gap:8px;text-shadow:0 1px 1px rgba(0,0,0,.25)}
.region-map{left:396px;top:161px;width:354px;height:404px;border:2px solid #fff;background:linear-gradient(135deg,var(--map-light) 0%,var(--map-light) 45%,var(--map-dark) 55%,var(--map-dark) 100%)}
.listing-photo{left:765px;width:133px;border:2px solid #fff;background:linear-gradient(#a9c7e4 0%,#d8d0bd 55%,#7f8a5e 100%);box-shadow:0 0 2px rgba(0,0,0,.3)}
.listing-photo.active{border-color:var(--title-blue)}
.ribbon{right:0;top:0;width:40px;height:40px;overflow:hidden}
.ribbon::before{content:"";position:absolute;right:-16px;top:8px;width:70px;height:12px;background:#1e8fd5;transform:rotate(40deg)}
.listing-data{left:914px;font-size:12px;line-height:16px;color:#111}
.listing-data dt{float:left;clear:left;width:48px;font-weight:700}
.listing-data dd{margin-left:48px}
.alert{left:397px;top:575px;width:336px;height:51px;background:var(--alert-bg);border-radius:2px}
.alert-text{left:60px;top:9px;width:270px;font-size:12px;line-height:15px;color:var(--alert-red)}
.site-footer{left:0;top:640px;width:1200px;height:155px;background:var(--navy)}
.footer-bar{left:0;top:795px;width:1200px;height:40px;background:var(--navy-dark);color:#8a9bb4;font-size:11px;text-align:center;line-height:40px}
.footer-title{font-size:13px;font-weight:600;color:var(--footer-text)}
.footer-links{list-style:none;font-size:12px;font-weight:600;color:var(--footer-text)}
.footer-links li{height:21px;padding-left:8px;position:relative}
.footer-links li::before{content:"";position:absolute;left:0;top:6px;border-left:3px solid var(--footer-text);border-top:3px solid transparent;border-bottom:3px solid transparent}
.footer-divider{left:598px;top:660px;width:1px;height:110px;background:rgba(0,0,0,.25);box-shadow:1px 0 0 rgba(255,255,255,.08)}
.contact{font-size:12px;color:var(--footer-text);line-height:21px}
.contact strong{font-size:14px;font-weight:600}
.contact-table{font-size:12px;color:var(--footer-text);line-height:21px}
.contact-table dt{float:left;clear:left;width:68px}
.contact-table a{color:var(--footer-text)}
</style>
</head>
<body>
<div class="abs backdrop" role="img" aria-label="Mapa claro da região ao fundo"></div>

<aside>
  <div class="abs sidebar"></div>
  <div class="abs sidebar-shadow"></div>
  <div class="abs brand"><span class="brand-mark"></span><span class="brand-name">Lartécnica</span></div>
  <ul class="abs main-menu">
    <li>A empresa</li><li>Localizacao</li><li>Area Restrita</li><li>Fale Conosco</li>
    <li>Cadastre seu imovel</li><li>Informacoes ao Proprietario</li><li>Informacoes ao Locatario</li><li>Solicite seu imovel</li>
  </ul>
  <div class="abs sidebar-rule"></div>
  <svg class="abs phone-icon" width="42" height="40" viewBox="0 0 42 40" aria-hidden="true">
    <path d="M3 10 Q21 -2 39 10 L35 16 L29 13 L29 9 Q21 6 13 9 L13 13 L7 16 Z" fill="#fff"/>
    <g fill="#fff"><circle cx="13" cy="21" r="2.5"/><circle cx="21" cy="21" r="2.5"/><circle cx="29" cy="21" r="2.5"/>
    <circle cx="13" cy="28" r="2.5"/><circle cx="21" cy="28" r="2.5"/><circle cx="29" cy="28" r="2.5"/>
    <circle cx="13" cy="35" r="2.5"/><circle cx="21" cy="35" r="2.5"/><circle cx="29" cy="35" r="2.5"/></g>
  </svg>
  <div class="abs phones">(48) 3555 0142<br>(48) 9555 0187</div>
</aside>

<div class="abs account-links">Login &nbsp;|&nbsp; Help</div>

<section class="abs search-panel"></section>
<div class="abs section-title" style="left:426px;top:40px">Busca de imoveis</div>
<div class="abs select-box">Todos</div>
<div class="abs check on" style="left:637px;top:72px"></div>
<div class="abs check-label" style="left:662px;top:71px">Para comprar</div>
<div class="abs check" style="left:768px;top:72px"></div>
<div class="abs check-label" style="left:794px;top:71px">Para alugar</div>
<div class="abs search-btn">
  <svg width="18" height="16" viewBox="0 0 18 16" aria-hidden="true"><circle cx="7" cy="7" r="5" fill="none" stroke="#fff" stroke-width="2.5"/><path d="M11 10 L16 14" stroke="#fff" stroke-width="3" stroke-linecap="round"/></svg>
  Buscar
</div>

<div class="abs section-title" style="left:426px;top:133px">Buscar imovel po regiao (location)</div>
<div class="abs region-map" role="img" aria-label="Mapa de Florianópolis dividido nas regiões Continente, Norte, Centro, Leste e Sul"></div>

<div class="abs section-title" style="left:765px;top:133px">We Recomended</div>
<div class="abs listing-photo" style="top:164px;height:88px" role="img" aria-label="Foto de prédio residencial com palmeiras"><span class="abs ribbon"></span></div>
<div class="abs listing-photo active" style="top:268px;height:88px" role="img" aria-label="Foto de prédio residencial com palmeiras"></div>
<div class="abs listing-photo" style="top:373px;height:88px" role="img" aria-label="Foto de prédio residencial com palmeiras"><span class="abs ribbon"></span></div>
<div class="abs listing-photo" style="top:476px;height:88px" role="img" aria-label="Foto de prédio residencial com palmeiras"></div>

<dl class="abs listing-data" style="top:160px"><dt>Bairro:</dt><dd>Coqueiros</dd><dt>Cidade:</dt><dd>CONTINENTE</dd><dt>Valor:</dt><dd>2.060,00</dd><dt>Cond.:</dt><dd>330,00</dd><dt>IPTU:</dt><dd>87,89</dd></dl>
<dl class="abs listing-data" style="top:266px"><dt>Bairro:</dt><dd>Coqueiros</dd><dt>Cidade:</dt><dd>CONTINENTE</dd><dt>Valor:</dt><dd>2.060,00</dd><dt>Cond.:</dt><dd>330,00</dd><dt>IPTU:</dt><dd>87,89</dd></dl>
<dl class="abs listing-data" style="top:371px"><dt>Bairro:</dt><dd>Coqueiros</dd><dt>Cidade:</dt><dd>CONTINENTE</dd><dt>Valor:</dt><dd>2.060,00</dd><dt>Cond.:</dt><dd>330,00</dd><dt>IPTU:</dt><dd>87,89</dd></dl>
<dl class="abs listing-data" style="top:472px"><dt>Bairro:</dt><dd>Coqueiros</dd><dt>Cidade:</dt><dd>CONTINENTE</dd><dt>Valor:</dt><dd>2.060,00</dd><dt>Cond.:</dt><dd>330,00</dd><dt>IPTU:</dt><dd>87,89</dd></dl>

<div class="abs alert">
  <svg class="abs" style="left:12px;top:12px" width="30" height="26" viewBox="0 0 30 26" aria-hidden="true"><path d="M15 1 L29 25 L1 25 Z" fill="#f39a12" stroke="#b86a05"/><rect x="13.5" y="8" width="3" height="10" fill="#333"/><rect x="13.5" y="20" width="3" height="3" fill="#333"/></svg>
  <p class="abs alert-text"><strong>Allert!</strong> Lorem ipsum dolor sit amet, consect etuer adipiscing elit.</p>
</div>

<footer>
  <div class="abs site-footer"></div>
  <div class="abs footer-title" style="left:157px;top:655px">MENU</div>
  <ul class="abs footer-links" style="left:157px;top:683px"><li>A empresa</li><li>Localização</li><li>Área Restrita</li><li>Fale Conosco</li></ul>
  <ul class="abs footer-links" style="left:271px;top:683px"><li>Cadastre seu imóvel</li><li>Informações ao Proprietário</li><li>Informações ao Locatário</li><li>Solicite seu imóvel</li></ul>
  <div class="abs footer-title" style="left:465px;top:655px">CUSTOMERS</div>
  <ul class="abs footer-links" style="left:466px;top:683px"><li>Privacy</li><li>Terms of use</li><li>Contact Support</li><li>FAQ</li></ul>
  <div class="abs footer-divider"></div>
  <div class="abs footer-title" style="left:619px;top:655px">CONTACT</div>
  <address class="abs contact" style="left:620px;top:681px;font-style:normal"><strong>Lartécnica</strong><br>Rua das Acácias, 140<br>Esquina com a Rua Marcos Lima<br>Centro - Florianópolis</address>
  <dl class="abs contact-table" style="left:840px;top:679px"><dt>CEP :</dt><dd>88000-100</dd><dt>Fax :</dt><dd>(48) 3555-0199</dd><dt>Locação :</dt><dd>(48) 3555-0123</dd><dt>Email :</dt><dd><a href="mailto:contato@lartecnica-exemplo.com">contato@lartecnica-exemplo.com</a></dd></dl>
  <div class="abs footer-bar">© (C) 2013 - Lartécnica - Todos os direitos reservados.</div>
</footer>
</body>
</html>
```